KTV Consulting

Government/Entitlement Consulting Services- I assist developers obtain entitlements from local, state and federal government agencies so that they can build their projects. Often these projects are very complicated and political and may face community opposition.

Target Market(s)

Real Estate Developers

Industry/Entity Type

Business Consultant

Contact Information for Business Card

Dana Pelletier
Principal

Font styles to use
Serif
Sans Serif

Requirements
Must have
• Classy and professional appeal.
Nice to have
• I like a combination of a mat and glossy finish. I've seen that done with black and then a bold color for a pop, but am not 100% committed to that.

```html
<!DOCTYPE html>
<html lang="en">
<head>
<meta charset="utf-8">
<title>KTV Consulting – Business Card</title>
<link rel="stylesheet" href="https://fonts.googleapis.com/css2?family=Source+Sans+3:wght@400;600;700&display=swap">
<style>
  :root {
    --backdrop-top: #5e5e5e;
    --backdrop-bottom: #737373;
    --card-white: #ffffff;
    --brand-orange: #d86a0a;
    --ink: #4a4a4a;
    --rule: #9a9a9a;
  }
  * { margin: 0; padding: 0; box-sizing: border-box; }
  html, body {
    width: 1200px;
    height: 900px;
    overflow: hidden;
  }
  body {
    position: relative;
    background: linear-gradient(to bottom, var(--backdrop-top), var(--backdrop-bottom));
    font-family: "Source Sans 3", "Myriad Pro", Arial, sans-serif;
    color: var(--ink);
  }
  .card {
    position: absolute;
    top: 306px;
    width: 440px;
    height: 271px;
    border-radius: 12px;
  }
  .card-front { left: 149px; background: var(--card-white); }
  .card-back { left: 608px; background: var(--brand-orange); }

  .wordmark {
    position: absolute;
    left: 0;
    width: 100%;
    text-align: center;
    font-weight: 700;
    line-height: 1;
  }
  .wordmark span { display: block; }
  .card-front .wordmark { top: 24px; color: var(--brand-orange); }
  .card-front .wordmark-initials { font-size: 64px; letter-spacing: 2px; }
  .card-front .wordmark-word { font-size: 28px; margin-top: 0; letter-spacing: 0.5px; }
  .card-back .wordmark { top: 78px; color: var(--card-white); }
  .card-back .wordmark-initials { font-size: 86px; letter-spacing: 3px; }
  .card-back .wordmark-word { font-size: 36px; margin-top: 2px; letter-spacing: 0.5px; }

  .address {
    position: absolute;
    left: 35px;
    top: 132px;
    font-size: 13px;
    line-height: 16px;
  }
  .holder {
    position: absolute;
    right: 43px;
    top: 159px;
    text-align: right;
  }
  .holder-name {
    font-size: 15px;
    font-weight: 600;
    color: var(--brand-orange);
    line-height: 20px;
  }
  .holder-title {
    font-size: 13px;
    line-height: 16px;
    margin-top: 3px;
  }
  .divider {
    position: absolute;
    left: 37px;
    top: 178px;
    width: 359px;
    height: 1px;
    background: var(--rule);
  }
  .contacts {
    position: absolute;
    left: 35px;
    top: 193px;
    list-style: none;
    font-size: 13px;
    line-height: 16px;
  }
  .contacts li { display: flex; align-items: center; }
  .contacts svg { width: 9px; height: 9px; margin-right: 7px; fill: var(--brand-orange); }
</style>
</head>
<body>
  <section class="card card-front">
    <div class="wordmark">
      <span class="wordmark-initials">KTV</span>
      <span class="wordmark-word">CONSULTING</span>
    </div>
    <p class="address">418 Harbor View Lane<br>Sacramento, CA 95814.</p>
    <div class="divider"></div>
    <div class="holder">
      <p class="holder-name">Dana Pelletier</p>
      <p class="holder-title">Principal</p>
    </div>
    <ul class="contacts">
      <li>
        <svg viewBox="0 0 10 10" aria-hidden="true"><path d="M2 0.5 L3.6 2.6 L2.7 3.6 Q3.8 5.9 6.3 7.2 L7.3 6.3 L9.5 7.9 L8.4 9.5 Q3.5 9 0.5 1.6 Z"/></svg>
        916-555 014 278
      </li>
      <li>
        <svg viewBox="0 0 10 10" aria-hidden="true"><path d="M0.5 2 H9.5 V8 H0.5 Z M1 2.5 L5 5.5 L9 2.5" stroke="#fff" stroke-width="0.8"/></svg>
        dana@ktvconsult.com
      </li>
      <li>
        <svg viewBox="0 0 10 10" aria-hidden="true"><circle cx="5" cy="5" r="4.5"/><path d="M5 0.5 V9.5 M0.5 5 H9.5" stroke="#fff" stroke-width="0.8"/></svg>
        www.ktvconsult.com
      </li>
    </ul>
  </section>

  <section class="card card-back">
    <div class="wordmark">
      <span class="wordmark-initials">KTV</span>
      <span class="wordmark-word">CONSULTING</span>
    </div>
  </section>
</body>
</html>
```